Business Card for premium dental clinic

We are a premium dental clinic based in Brasov, Romania with more than 15 year on the market, providing quality dental treatment made by a team of more specialized dentists, working with modern equipment as a solution to beautiful and healthy teeth.

Our current logo for the clinic use 2 square with colors black and gold - dr Corbescu - studio, using family fonts Bodoni, Myriad Pro and Segoe Print.
Depending on the printing we used some gold CMYK background or gold foil picture background or a gold gradient.
We want a business card:
- eye catching business card
- distinguished business card
- premium design
- to keep the color scheme of black and gold
- to attract the customers to spent time reading the information
- modern concept

```html
<!DOCTYPE html>
<html lang="en">
<head>
<meta charset="utf-8">
<title>Arcada Dental – Business Card</title>
<link href="https://fonts.googleapis.com/css2?family=Roboto+Condensed:wght@300;400&family=Roboto:wght@400&display=swap" rel="stylesheet">
<style>
  :root {
    --backdrop: #3b3b3d;
    --card-dark: #2c2c2e;
    --gold-light: #f6d873;
    --gold-mid: #e7b92e;
    --gold-deep: #b98512;
    --white: #ffffff;
    --ink: #1c1a14;
  }
  * { margin: 0; padding: 0; box-sizing: border-box; }
  html, body { width: 799px; height: 1200px; overflow: hidden; }
  body {
    background: var(--backdrop);
    font-family: "Roboto Condensed", "Arial Narrow", sans-serif;
  }
  .canvas { position: relative; width: 799px; height: 1200px; }

  .card {
    position: absolute;
    left: 50px;
    width: 700px;
    height: 400px;
    overflow: hidden;
    background: var(--card-dark);
    box-shadow: 0 14px 30px rgba(0,0,0,0.45);
  }
  .card--front { top: 95px; }
  .card--back  { top: 705px; }

  .gold-foil {
    position: absolute;
    top: 0; left: 0; height: 100%;
    background:
      radial-gradient(circle at 30% 35%, var(--gold-light) 0%, transparent 55%),
      radial-gradient(circle at 75% 80%, var(--gold-deep) 0%, transparent 60%),
      linear-gradient(135deg, var(--gold-mid), var(--gold-light) 45%, var(--gold-mid) 70%, var(--gold-deep));
  }
  .card--front .gold-foil { width: 330px; }
  .card--back  .gold-foil { width: 420px; }

  .name-plate {
    position: absolute;
    background: var(--white);
    color: var(--ink);
    font-weight: 300;
    display: flex;
    align-items: center;
    justify-content: center;
    letter-spacing: -0.5px;
    white-space: nowrap;
  }
  .name-plate .title { font-size: 0.6em; margin-right: 4px; }
  .card--front .name-plate { left: 34px; top: 112px; width: 296px; height: 96px; font-size: 54px; }
  .card--back  .name-plate { left: 40px; top: 26px; width: 232px; height: 66px; font-size: 38px; }

  .brand-name {
    position: absolute;
    color: var(--white);
    font-weight: 400;
    text-align: center;
    line-height: 1.05;
  }
  .card--front .brand-name { left: 330px; width: 370px; top: 135px; font-size: 56px; }
  .card--back  .brand-name { left: 380px; width: 320px; top: 140px; font-size: 54px; }

  .back-shape { position: absolute; inset: 0; width: 700px; height: 400px; }

  .contact-list {
    position: absolute;
    left: 40px;
    top: 188px;
    list-style: none;
    font-family: "Roboto", Arial, sans-serif;
    font-size: 15px;
    color: var(--ink);
    line-height: 24px;
  }
  .contact-list li { display: flex; align-items: center; gap: 10px; }
  .contact-list .icon { width: 14px; height: 14px; flex: none; }
  .contact-list .address { padding-left: 0; margin-top: 2px; }
</style>
</head>
<body>
<main class="canvas">

  <section class="card card--front" aria-label="Business card front">
    <div class="gold-foil" role="img" aria-label="Crumpled gold foil texture"></div>
    <div class="name-plate"><span class="title">dr.</span>corbescu</div>
    <div class="brand-name">Arcada<br>Dental</div>
  </section>

  <section class="card card--back" aria-label="Business card back">
    <div class="gold-foil" role="img" aria-label="Crumpled gold foil texture"></div>
    <svg class="back-shape" viewBox="0 0 700 400" aria-hidden="true">
      <path d="M700 0 L400 0 Q300 170 350 400 L700 400 Z" fill="#ffffff"/>
      <path d="M700 0 L404 0 Q318 180 372 400 L700 400 Z" fill="#2c2c2e"/>
    </svg>
    <div class="name-plate"><span class="title">dr.</span>corbescu</div>

    <ul class="contact-list">
      <li>
        <svg class="icon" viewBox="0 0 16 16"><path d="M3 1h3l1.5 4-2 1.3a9 9 0 0 0 4.2 4.2L11 8.5l4 1.5v3a2 2 0 0 1-2 2A13 13 0 0 1 1 3a2 2 0 0 1 2-2z" fill="#1c1a14"/></svg>
        0268-410-227
      </li>
      <li>
        <svg class="icon" viewBox="0 0 16 16"><rect x="1" y="3" width="14" height="10" fill="#1c1a14"/><path d="M1 3l7 6 7-6" stroke="#e7b92e" stroke-width="1.3" fill="none"/></svg>
        contact@arcadadental.ro
      </li>
      <li>
        <svg class="icon" viewBox="0 0 16 16"><circle cx="8" cy="8" r="6.5" fill="none" stroke="#1c1a14" stroke-width="1.5"/><path d="M1.5 8h13M8 1.5c-3 3.5-3 9.5 0 13M8 1.5c3 3.5 3 9.5 0 13" stroke="#1c1a14" stroke-width="1.2" fill="none"/></svg>
        www.arcadadental.ro
      </li>
      <li class="address">12 Str. Lungă, Brașov,</li>
      <li class="address">Romania 500035</li>
    </ul>

    <div class="brand-name">Arcada<br>Dental</div>
  </section>

</main>
</body>
</html>
```